Nutritional neuroscience book cover design*

We need a book cover design for a new book on nutritional neuroscience and aging. The book is written for the general public and answers questions such as, "We are living longer than ever. The problem is, will our brain stay healthy as we age? We certainly do not want to live longer with various diseases, in particular brain diseases. How does the brain change during aging? And what can we do to promote the health of our brain and prevent and treat neurological diseases that typically occur during the aging process?" Based on recent discoveries in the field of nutritional neuroscience, this book presents how we can use nutrition to help our brain stay healthy longer. While our brain shrinks and becomes functionally weaker during the aging process, nutrition is able to slow this process down. This book illustrates this point through chapters on stroke, Parkinson’s disease, Multiple Sclerosis, dementia, depression, anxiety, and schizophrenia. The book will appeal to anyone looking to optimize their brain’s health and performance today and decades into the future.

Target Market(s)

General audience

Colors

Designer to choose colors to be used in the design.

Requirements
Must have
• Title: Meals Across the Decades: A Companion Guide to Dietary Brain Science Today
• Edited by Odelia R. Vantrosk, Ph.D.
• Book size: 7*10 inches
• Backcover text:
• Humans are living longer than ever. How does the brain change during aging? Will our brain stay healthy as we age? We certainly do not want to live longer with neurological diseases. What can we do to promote the health of our brain?
• Based on recent discoveries in the field of nutritional neuroscience, this book presents how nutrition affects our brain health. While we age, our brain shrinks and there are changes in how it functions, nutrition is an important component that can help maintain optimal brain health.
• Using scientific evidence, this book illustrates the importance of nutrition for neurological diseases including Alzheimer’s disease, stroke, Parkinson’s disease, Multiple Sclerosis, vascular dementia, depression, anxiety, and schizophrenia. This book will appeal to anyone looking to learn more about how nutrition affects brain health.

```html
<!DOCTYPE html>
<html lang="en">
<head>
<meta charset="utf-8">
<title>Meals Across the Decades — Book Cover</title>
<link rel="stylesheet" href="https://fonts.googleapis.com/css2?family=League+Gothic&display=swap">
<style>
  :root {
    --paper: #f8f7f1;
    --slate: #86a0b0;
    --title-yellow: #fde07b;
    --title-shadow: #3e5574;
    --plate: #fbfaf4;
    --brain: #bf8f6d;
    --cutlery: #b9b5ad;
    --author: #ffffff;
  }
  html, body {
    margin: 0;
    padding: 0;
    width: 846px;
    height: 1200px;
    overflow: hidden;
    background: var(--paper);
  }
  .cover {
    position: relative;
    width: 846px;
    height: 1200px;
    background: var(--paper);
    font-family: "League Gothic", "Oswald", sans-serif;
  }
  .cover-panel {
    position: absolute;
    left: 22px;
    top: 14px;
    width: 802px;
    height: 1162px;
    background: var(--slate);
  }
  .title {
    position: absolute;
    left: 0;
    top: 52px;
    width: 846px;
    margin: 0;
    text-align: center;
    font-weight: 400;
    font-size: 128px;
    line-height: 114px;
    letter-spacing: -1px;
    text-transform: uppercase;
    color: var(--title-yellow);
    text-shadow: -6px 6px 0 var(--title-shadow);
  }
  .title span { display: block; }
  .place-setting {
    position: absolute;
    left: 0;
    top: 0;
  }
  .subtitle {
    position: absolute;
    left: 0;
    top: 1010px;
    width: 846px;
    margin: 0;
    text-align: center;
    font-weight: 400;
    font-size: 44px;
    line-height: 1;
    color: var(--title-yellow);
    text-shadow: -3px 3px 0 var(--title-shadow);
  }
  .author {
    position: absolute;
    left: 0;
    top: 1116px;
    width: 846px;
    margin: 0;
    text-align: center;
    font-weight: 400;
    font-size: 50px;
    line-height: 1;
    letter-spacing: 0.5px;
    color: var(--author);
  }
</style>
</head>
<body>
  <div class="cover">
    <div class="cover-panel"></div>

    <h1 class="title">
      <span>Meals</span>
      <span>Across the</span>
      <span>Decades</span>
    </h1>

    <svg class="place-setting" width="846" height="1200" viewBox="0 0 846 1200" aria-hidden="false">
      <circle class="plate" cx="423" cy="720" r="243" fill="var(--plate)"/>
      <ellipse class="brain-art" cx="426" cy="714" rx="166" ry="193" fill="var(--brain)"
               role="img" aria-label="Illustration of a human brain seen from above, served on the plate"/>
      <rect class="fork-art" x="86" y="536" width="58" height="400" rx="26" fill="var(--cutlery)"
            role="img" aria-label="Illustration of a fork to the left of the plate"/>
      <rect class="knife-art" x="718" y="521" width="46" height="427" rx="22" fill="var(--cutlery)"
            role="img" aria-label="Illustration of a knife to the right of the plate"/>
    </svg>

    <p class="subtitle">A Companion Guide to Dietary Brain Science Today</p>
    <p class="author">Odelia R. Vantrosk</p>
  </div>
</body>
</html>
```